Rabbit Meat Flyer

Lower in fat than many other meats, low in lipids (av. = 6g per 100g meat, notably the fillet and thigh joints).

A meat rich in quality proteins (around 21g per 100g) it is also lower in calories and sodium than the majority of other meats.

An excellent source of vitamins, minerals and trace elements: High in vitamins B3 and B12, phosphorus, potassium and selenium. It contributes to a good balance of vitamins and minerals for daily dietary requirements.

A meat with an excellent balance of fatty acids (rabbit is richer in omega 3 than chicken* or pork*. It has a moderate fat content (depending on the type of cut).

Compared to beef, pork, lamb, turkey, veal, and chicken, rabbit has the highest percentage of protein, the lowest percentage of fat, and the fewest calories per pound. The alfalfa-loving herbivores are foragers (which means they don’t rely on energy-intensive soy or corn for food) that grow and reproduce quickly. According to Brindle Harvest Guild, “rabbit can produce six pounds of meat on the same amount of feed and water it takes a cow to produce just one pound

```html
<!DOCTYPE html>
<html lang="en">
<head>
<meta charset="utf-8">
<title>Rabbit Meat Flyer</title>
<link rel="stylesheet" href="https://fonts.googleapis.com/css2?family=Kaushan+Script&family=Didact+Gothic&family=Orbitron:wght@600&display=swap">
<style>
  :root {
    --ink: #000000;
    --paper: #ffffff;
    --accent-red: #e14a58;
    --text-red: #ee3d4c;
    --text-yellow: #f4d11f;
    --roast-dark: #4a2c1c;
    --roast-mid: #8a5a36;
    --roast-light: #b9885a;
  }
  * { margin: 0; padding: 0; box-sizing: border-box; }
  html, body { width: 848px; height: 1200px; overflow: hidden; background: var(--ink); }
  .flyer {
    position: relative; width: 848px; height: 1200px; overflow: hidden;
    background: var(--ink); color: var(--paper);
    font-family: "Didact Gothic", "Century Gothic", sans-serif;
  }
  .hero-photo {
    position: absolute; left: 0; top: 0; width: 848px; height: 390px;
    background: radial-gradient(ellipse at 55% 30%, var(--roast-light) 0%, var(--roast-mid) 40%, var(--roast-dark) 80%);
  }
  .header-arc { position: absolute; left: 0; top: 0; width: 848px; height: 1200px; }
  .title {
    position: absolute; left: 0; width: 848px; top: 282px; text-align: center;
    font-family: "Kaushan Script", cursive; font-weight: 400; font-size: 80px; line-height: 1;
    letter-spacing: 3px; color: var(--paper); transform: rotate(-2deg);
  }
  .fact {
    position: absolute; font-size: 24px; line-height: 28px; letter-spacing: 0.8px;
    white-space: nowrap; padding-left: 17px;
  }
  .fact::before {
    content: ""; position: absolute; left: 1px; top: 10px;
    width: 9px; height: 9px; border-radius: 50%; background: var(--paper);
  }
  .fact--plain::before { display: none; }
  .hl-red { color: var(--text-red); }
  .hl-yellow { color: var(--text-yellow); }
  .fact-1 { left: 11px; top: 419px; }
  .fact-2 { left: 11px; top: 512px; }
  .fact-3 { left: 11px; top: 611px; }
  .fact-4 { left: 240px; top: 740px; }
  .fact-5 { left: 240px; top: 858px; }
  .fact-5-cont { left: 12px; top: 977px; padding-left: 0; }
  .dish-round {
    position: absolute; left: 603px; top: 394px; width: 178px; height: 178px;
    border-radius: 50%; border: 3px solid #5a5a5a;
    background: radial-gradient(circle, var(--roast-mid) 0%, var(--roast-dark) 60%, #1a1a1a 100%);
  }
  .dish-legs {
    position: absolute; left: 33px; top: 740px; width: 172px; height: 216px;
    border-radius: 0 108px 108px 0; border: 3px solid #8a8a8a; border-left: none;
    background: radial-gradient(ellipse at 40% 50%, var(--roast-light) 0%, var(--roast-mid) 45%, #1a1a1a 100%);
  }
  .footer-bar {
    position: absolute; left: 0; top: 1157px; width: 848px; height: 43px;
    background: var(--accent-red);
    display: flex; align-items: center; justify-content: space-between; padding: 0 14px 0 17px;
  }
  .brand-name {
    font-family: "Orbitron", sans-serif; font-weight: 600; font-size: 19px;
    letter-spacing: 3px; text-transform: uppercase; color: var(--paper);
  }
  .phone { font-size: 24px; letter-spacing: 1px; color: var(--paper); }
</style>
</head>
<body>
<main class="flyer">
  <div class="hero-photo" role="img" aria-label="Roasted rabbit pieces on a grey plate with rosemary sprigs and lemon halves"></div>
  <svg class="header-arc" viewBox="0 0 848 1200" aria-hidden="true">
    <path d="M0,339 Q424,152 848,301 L848,1200 L0,1200 Z" fill="var(--accent-red)"/>
    <path d="M0,381 Q424,156 848,363 L848,1200 L0,1200 Z" fill="var(--ink)"/>
  </svg>
  <h1 class="title">RABBIT MEAT</h1>

  <div class="dish-round" role="img" aria-label="Bowl of roasted rabbit pieces with rosemary"></div>
  <div class="dish-legs" role="img" aria-label="Seasoned roasted rabbit legs"></div>

  <p class="fact fact-1">Lower in fat than many other meats,<br>low in lipids (av. = 6g per 100g meat,<br>notably the fillet and thigh joints).</p>
  <p class="fact fact-2">A meat rich in quality proteins<br>(around 21g per 100g) it is also lower in<br>calories and sodium than the majority of other meats.</p>
  <p class="fact fact-3">An excellent <span class="hl-red">source of vitamins</span>, <span class="hl-red">minerals</span> and trace<br>elements: High in vitamins B3 and B12, phosphorus,<br>potassium and selenium.It contributes to a good balance<br>of vitamins and minerals for daily dietary requirements.</p>
  <p class="fact fact-4">A meat with an excellent balance of<br>fatty acids (rabbit is <span class="hl-yellow">richer</span> in omega 3<br>than chicken* or pork*. It has a moderate<br>fat content (depending on the type of cut).</p>
  <p class="fact fact-5">Compared to beef, pork, lamb, turkey, veal,<br>and chicken, rabbit has the <span class="hl-red">highest</span><br><span class="hl-red">percentage of</span> protein, the <span class="hl-yellow">lowest</span><br><span class="hl-yellow">percentage of</span> fat, and the fewest</p>
  <p class="fact fact--plain fact-5-cont">calories per pound. The alfalfa-loving herbivores are foragers<br>(which means they don’t rely on energy-intensive soy or corn<br>for food) that grow and reproduce quickly. According to<br>Brindle Harvest Guild, “rabbit can produce six pounds of meat<br>on the same amount of feed and water it takes a cow to<br>produce just one pound</p>

  <footer class="footer-bar">
    <span class="brand-name">Fernhollow Meats</span>
    <span class="phone">Phone : +1 555 0100</span>
  </footer>
</main>
</body>
</html>
```